Business Card & Stationary Design Project

We are looking for some creative direction for business cards and our stationary.

We are a global logistics firm that has recently changed its name to Marrick Global Logistics and we have a new website due out tomorrow (www.marrick.com.au).

The colours of the company are rich navy tones, I would like to have business cards that fit together to make one picture on the back (possibly an old map of the world??), and the front to be modern contemporary looking.

But I am open to suggestions, so just incorporate our new logo and get going!
Updates

Hi Everyone,

Thank you for all of your designs so far and the time you have put into it.

I have asked many of you for amendments to see if we can get a final product, so with this in mind I am extending the deadline by a few days.

Good luck and thank you once again.

Please message me direct if you need any clarification.

Kind Regards
Colin

Reason: As outlined the extra 3 days is for amendments and changes to the current submissions. Thanks Colin

Industry/Entity Type

Business

```html
<!DOCTYPE html>
<html lang="en">
<head>
<meta charset="utf-8">
<title>Marrick Global Logistics – Business Card &amp; Letterhead</title>
<link rel="stylesheet" href="https://fonts.googleapis.com/css2?family=Cinzel:wght@400&display=swap">
<style>
  :root {
    --navy-deep: #06184a;
    --navy-mid: #0d2f73;
    --navy-bar: #0b0d6b;
    --accent-blue: #2f7fd6;
    --paper: #ffffff;
    --stage: #eeeeef;
    --map-light: #e4e4e4;
    --map-dark: #b9b9b9;
    --ink: #1c1c1c;
    --footer-ink: #f4f4f4;
  }
  * { box-sizing: border-box; margin: 0; padding: 0; }
  html, body { width: 1200px; height: 848px; overflow: hidden; }
  body {
    background: var(--stage);
    font-family: "Cinzel", "Times New Roman", serif;
    font-weight: 400;
    position: relative;
  }

  .card, .letterhead { position: absolute; background: var(--paper); overflow: hidden; }

  /* Company name set plainly in the text font */
  .company-name {
    position: absolute;
    color: var(--navy-bar);
    font-weight: 400;
    line-height: 1;
    white-space: nowrap;
  }

  /* Business card – front */
  .card-front {
    left: 126px; top: 168px; width: 377px; height: 227px;
    background: radial-gradient(ellipse 55% 70% at 50% 50%, var(--navy-mid), var(--navy-deep));
  }
  .card-front .name-band {
    position: absolute; left: 0; right: 0; top: 79px; height: 58px;
    background: var(--paper);
  }
  .card-front .company-name {
    left: 0; right: 0; top: 21px; text-align: center; font-size: 15px;
  }

  /* Business card – back */
  .card-back { left: 126px; top: 423px; width: 377px; height: 226px; }
  .card-back .map-field {
    position: absolute; inset: 0;
    background: radial-gradient(ellipse 70% 80% at 40% 45%, var(--map-light), var(--map-dark));
  }
  .card-back .contact {
    position: absolute; left: 30px; top: 98px;
    font-style: normal; font-size: 8.5px; color: var(--ink);
    line-height: 11px; letter-spacing: 0.02em;
  }
  .card-back .name-band {
    position: absolute; left: 232px; right: 0; top: 99px; height: 43px;
    background: var(--paper);
  }
  .card-back .company-name {
    left: 0; right: 0; top: 16px; text-align: center; font-size: 9.5px;
  }

  /* Letterhead */
  .letterhead { left: 575px; top: 75px; width: 499px; height: 645px; }
  .letterhead .header-bar {
    position: absolute; left: 0; top: 27px; width: 367px; height: 16px;
    background: var(--navy-bar);
  }
  .letterhead .company-name {
    left: 372px; top: 31px; font-size: 7.5px;
  }
  .letterhead .header-tab {
    position: absolute; left: 481px; top: 28px; width: 18px; height: 13px;
    background: var(--accent-blue);
  }
  .letterhead .footer-band {
    position: absolute; left: 0; right: 0; bottom: 0; height: 56px;
    background: linear-gradient(90deg, #bdbdbd, #d2d2d2 50%, #c0c0c0);
  }
  .letterhead .footer-address {
    position: absolute; left: 30px; top: 11px;
    font-size: 5px; color: var(--footer-ink);
  }
  .letterhead .footer-contact {
    position: absolute; left: 104px; top: 10px;
    font-style: normal; font-size: 5px; color: var(--footer-ink); line-height: 7px;
  }
</style>
</head>
<body>
  <section class="card card-front" aria-label="Business card front">
    <div class="name-band">
      <span class="company-name">Marrick Global Logistics</span>
    </div>
  </section>

  <section class="card card-back" aria-label="Business card back">
    <div class="map-field" role="img" aria-label="Faint antique map of the world in soft greys"></div>
    <address class="contact">
      Company Address<br>
      Phone : 01234 567 89 | Fax: 01234 567 89<br>
      johndoe@companyname.com<br>
      www.yourcompanynmae.com
    </address>
    <div class="name-band">
      <span class="company-name">Marrick Global Logistics</span>
    </div>
  </section>

  <section class="letterhead" aria-label="Letterhead">
    <div class="header-bar"></div>
    <span class="company-name">Marrick Global Logistics</span>
    <div class="header-tab"></div>
    <footer class="footer-band" role="img" aria-label="Faint antique world map band with contact details">
      <span class="footer-address">Company Address</span>
      <address class="footer-contact">
        Phone : 01234 567 89 | Fax: 01234 567 89<br>
        johndoe@companyname.com<br>
        www.yourcompanynmae.com
      </address>
    </footer>
  </section>
</body>
</html>
```